Need Business Card for our Indian Grocery Store

Industry/Entity Type

Grocery Store

Contact Information for Business Card

Manoj Baweja
Director

Store Locations:

Thomastown
482 Elm Parade
P: 03 9172 5843

Kellbrook
613 Carlow Road
P: 03 9238 6014

email: kvtmarts@mailnest.example

Requirements
Must have
• Our logo Colours

```html
<!DOCTYPE html>
<html lang="en">
<head>
<meta charset="utf-8">
<title>KVT Groceries &amp; Spices – Business Card</title>
<link href="https://fonts.googleapis.com/css2?family=Roboto:wght@300;400;700&display=swap" rel="stylesheet">
<style>
  :root {
    --backdrop: #2a2c30;
    --card-white: #ffffff;
    --brand-red: #e3312f;
    --brand-red-deep: #d4161b;
    --icon-red: #c8101a;
    --ink-grey: #3a3a3a;
    --ink-soft: #6b6b6b;
  }
  * { margin: 0; padding: 0; box-sizing: border-box; }
  html, body {
    width: 1200px; height: 900px; overflow: hidden;
    background: var(--backdrop);
    font-family: "Roboto", Arial, sans-serif;
  }
  .canvas {
    position: relative; width: 1200px; height: 900px;
  }
  .card {
    position: absolute; left: 250px; width: 700px; height: 400px;
    border-radius: 22px; overflow: hidden;
    box-shadow: 0 14px 30px rgba(0,0,0,.45);
  }
  .card--front { top: 40px; background: var(--card-white); }
  .card--back { top: 460px; background: var(--brand-red-deep); }

  /* Front */
  .person { position: absolute; left: 52px; top: 52px; }
  .person__name { font-size: 36px; letter-spacing: .5px; text-transform: uppercase; }
  .person__first { font-weight: 300; color: var(--ink-grey); }
  .person__last { font-weight: 700; color: var(--brand-red-deep); }
  .person__role {
    margin-top: 4px; font-size: 15px; font-weight: 400;
    letter-spacing: 4px; color: var(--ink-soft); text-transform: uppercase;
  }

  .brand {
    position: absolute; right: 44px; top: 118px;
    display: flex; align-items: center; gap: 12px;
  }
  .brand__mark { width: 22px; height: 22px; background: var(--brand-red-deep); }
  .brand__name {
    font-size: 24px; font-weight: 700; color: var(--brand-red-deep);
    text-transform: uppercase; letter-spacing: 1px;
  }

  .locations-title {
    position: absolute; left: 372px; top: 212px;
    font-size: 17px; font-weight: 700; letter-spacing: 3px;
    color: var(--brand-red-deep); text-transform: uppercase;
  }

  .stripe-thin {
    position: absolute; left: 0; right: 0; top: 244px; height: 9px;
    background: var(--brand-red);
  }
  .contact-band {
    position: absolute; left: 0; right: 0; top: 262px; height: 110px;
    background: var(--brand-red);
  }
  .icon-column {
    position: absolute; left: 318px; top: 0; width: 44px; height: 110px;
    display: flex; flex-direction: column;
  }
  .icon-cell {
    flex: 1; display: flex; align-items: center; justify-content: center;
    background: var(--icon-red);
  }
  .icon-cell + .icon-cell { border-top: 2px solid var(--brand-red); }
  .contact-row {
    position: absolute; left: 0; right: 0; height: 55px;
    display: flex; align-items: center;
    color: var(--card-white); font-size: 16px; font-weight: 400;
  }
  .contact-row--phone { top: 0; }
  .contact-row--address { top: 55px; }
  .contact-row__left { width: 300px; text-align: right; }
  .contact-row__right { margin-left: 80px; }

  /* Back */
  .back-brand {
    position: absolute; inset: 0;
    display: flex; align-items: center; justify-content: center; gap: 16px;
  }
  .back-brand__mark { width: 30px; height: 30px; background: var(--card-white); }
  .back-brand__name {
    font-size: 40px; font-weight: 700; color: var(--card-white);
    text-transform: uppercase; letter-spacing: 1.5px;
  }
</style>
</head>
<body>
<main class="canvas">

  <section class="card card--front" aria-label="Business card front">
    <div class="person">
      <h1 class="person__name"><span class="person__first">Manoj</span> <span class="person__last">Baweja</span></h1>
      <p class="person__role">Director</p>
    </div>

    <div class="brand">
      <span class="brand__mark" aria-hidden="true"></span>
      <span class="brand__name">KVT Groceries &amp; Spices</span>
    </div>

    <h2 class="locations-title">Locations</h2>

    <div class="stripe-thin"></div>
    <div class="contact-band">
      <div class="icon-column" aria-hidden="true">
        <div class="icon-cell">
          <svg width="20" height="20" viewBox="0 0 24 24"><path fill="#fff" d="M6.6 10.8a15.1 15.1 0 0 0 6.6 6.6l2.2-2.2c.3-.3.7-.4 1-.2 1.1.4 2.3.6 3.6.6.6 0 1 .4 1 1V20c0 .6-.4 1-1 1A17 17 0 0 1 3 4c0-.6.4-1 1-1h3.5c.6 0 1 .4 1 1 0 1.3.2 2.5.6 3.6.1.3 0 .7-.2 1l-2.3 2.2z"/></svg>
        </div>
        <div class="icon-cell">
          <svg width="20" height="20" viewBox="0 0 24 24"><path fill="#fff" d="M12 2a7 7 0 0 0-7 7c0 5.2 7 13 7 13s7-7.8 7-13a7 7 0 0 0-7-7zm0 9.5A2.5 2.5 0 1 1 12 6.5a2.5 2.5 0 0 1 0 5z"/></svg>
        </div>
      </div>
      <div class="contact-row contact-row--phone">
        <span class="contact-row__left">03 9172 5843</span>
        <span class="contact-row__right">03 9238 6014</span>
      </div>
      <div class="contact-row contact-row--address">
        <span class="contact-row__left">Ashby Vale, 482 Elm Parade</span>
        <span class="contact-row__right">Kellbrook, 613 Carlow Road</span>
      </div>
    </div>
  </section>

  <section class="card card--back" aria-label="Business card back">
    <div class="back-brand">
      <span class="back-brand__mark" aria-hidden="true"></span>
      <span class="back-brand__name">KVT Groceries &amp; Spices</span>
    </div>
  </section>

</main>
</body>
</html>
```